Modern Small Law Firm Website To Look Cutting Edge

I need a website design for a new, single-attorney law firm. The firm will be called "The Thornwell Law Group." Our goal is to handle car accident and general personal injury lawsuits for individuals.

Our selling points are: (1) We charge less so you keep more; (2) We have experience and success trying and settling multi-million dollar cases; (3) We use modern technology to make the whole process simple, easy and hassle-free for clients.

Also because we are a one-man law firm, the clients will personally know the lawyer and have access to them. For that reason, I thought a good big tagline for the website would be "KNOW YOUR LAWYER"

I like the idea of splitting the website vertically down the middle, with the left side having a blue background, a picture of me, and big white lettering for the tagline, and the right side having a white background with blue lettering and headlines. I don't want navy blue or royal blue, but a more bright and eye-catching blue color. We can experiment with different shades.

I would be curious about how it could look with some minor orange accent coloring somewhere.

I need to feature prominently, probably in the top left corner, this phone number: 504-917-2083.

This will be used as much by mobile users as it would be by desktop/computer users.

The final design should communicate trust, convenience and cutting edge technology that leads to success.

Finally, I would be curious how we can have a sleek looking info submission box somewhere on the right side nearer the bottom that features different combinations of presenting these phrases: "QUICK QUESTION? QUICK ANSWER" The info submission button could say "Ask"

I am uploading two different pictures of me that can be used. The gray backgrounds are not necessary or good, if there is a way to cut them out that would be great. I can try and get that if needed.

Target Market(s)

Individuals who have been hurt by others, mostly in car accidents. They will be frustrated, inconvenienced and need to be soothed.

Industry/Entity Type

Legal

Number of Pages Required

1 page

Font styles to use
Sans Serif

Colors
0692cd
33a6d7
85cae6
faa54b
f78f20
3276b5

Requirements
Must have
• If you have started designing already, please note that the project description information is more important than the image that I uploaded originally. It has since been deleted.
• Also please now use the color photo that has been uploaded.
Nice to have
• I really want a clean and simple website design with not a lot of clutter. I'd like to avoid the typical law firm websites that you see that have tool bars across the top and basic borders/columns everywhere. It needs to grab your attention and look a little more cutting edge and different.
• Let's experiment with different eye-catching ways to present the three value propositions I noted.
• Also if the screen is split vertically with the left and right side being blue and white, maybe we can experiment with different ways that the two colors could fade into each other as opposed to just a line where one color starts and the other ends.
• And maybe the blue/white backgrounds could be textured somehow so that they don't appear flat. Perhaps we could try using differing shades of blue to give the appearance of pattern or 3D texture.
Should not have
• The basic picture/design I uploaded is just a suggestion, but there isn't really anything there.

```html
<!DOCTYPE html>
<html lang="en">
<head>
<meta charset="utf-8">
<title>The Thornwell Law Group</title>
<link href="https://fonts.googleapis.com/css2?family=Montserrat:wght@400;600;700&family=Lato:ital,wght@0,400;0,700;1,400&family=Oswald:wght@400&display=swap" rel="stylesheet">
<style>
:root{
  --red:#e8212b;
  --red-dark:#b9161e;
  --blue:#0652a5;
  --blue-bright:#1a7de2;
  --blue-frame:#3a78c4;
  --orange:#f0873a;
  --ink:#1e1e1e;
  --grey-text:#6a6a6a;
  --band-grey:#efefef;
  --footer:#474747;
  --footer-bottom:#3b3b3b;
  --footer-text:#cfcfcf;
  --card-dark:#2f3530;
  --white:#ffffff;
}
*{margin:0;padding:0;box-sizing:border-box}
html,body{width:1200px;height:2225px;overflow:hidden}
body{position:relative;background:var(--white);font-family:'Lato',sans-serif;color:var(--ink)}
.abs{position:absolute}

/* header */
.site-header{left:0;top:0;width:1200px;height:80px;background:var(--white)}
.brand{left:156px;top:20px;font-family:'Montserrat',sans-serif;font-weight:600;font-size:21px;color:var(--ink);letter-spacing:.2px}
.social-top{left:664px;top:29px;display:flex;gap:6px}
.social-dot{width:24px;height:24px;border-radius:50%;background:#cfcfcf}
.social-dot.is-active{background:var(--red)}
.call{left:828px;top:22px;display:flex;align-items:center;gap:6px;font-family:'Oswald',sans-serif;font-size:26px;color:var(--ink)}
.call .call-label{color:var(--red)}

/* navigation */
.main-nav{left:0;top:80px;width:1200px;height:42px;background:var(--red)}
.main-nav ul{list-style:none;position:absolute;left:156px;top:0;height:42px;display:flex}
.main-nav li{height:42px;line-height:42px;font-family:'Montserrat',sans-serif;font-size:11px;font-weight:600;color:var(--white);padding:0 15px;letter-spacing:.3px;margin-right:14px}
.main-nav li.is-current{background:var(--red-dark);color:#ff6b70;padding:0 18px}

/* hero */
.hero{left:0;top:122px;width:1200px;height:360px;background:linear-gradient(100deg,#2c2926 0%,#4a423a 35%,#7d6a58 60%,#3a342f 100%)}
.hero-title{left:156px;top:240px;font-family:'Montserrat',sans-serif;font-size:29px;font-weight:600;color:var(--white)}
.hero-text{left:156px;top:290px;width:580px;font-size:14px;line-height:19px;color:#f2f2f2}
.read-more{font-family:'Montserrat',sans-serif;font-size:11px;font-weight:600;letter-spacing:1px;display:flex;align-items:center;gap:6px}
.hero .read-more,.hero-more{color:var(--white)}
.hero-more{left:156px;top:342px}
.arrow-left{left:84px;top:290px}
.arrow-right{left:1092px;top:290px}

/* testimonials */
.testimonials{left:0;top:482px;width:1200px;height:267px;background:var(--band-grey)}
.section-label{left:156px;top:518px;font-family:'Montserrat',sans-serif;font-weight:600;font-size:14px}
.quote{left:156px;top:555px;width:510px;font-style:italic;font-size:13px;line-height:17px;color:var(--grey-text)}
.avatar{left:156px;top:641px;width:74px;height:74px;border-radius:50%;background:radial-gradient(circle,#c9a68f 0%,#7a5a48 60%,#f4f4f4 62%);border:3px solid #fff;box-shadow:0 1px 4px rgba(0,0,0,.15)}
.client-name{left:255px;top:669px;font-size:15px;color:var(--blue-bright)}
.slider-dots{left:619px;top:674px;display:flex;gap:3px}
.slider-dots span{width:8px;height:8px;border-radius:50%;border:1px solid #888}
.slider-dots span.is-on{background:#555}

/* quick question */
.ask-card{left:764px;top:402px;width:279px;height:411px;filter:drop-shadow(0 4px 8px rgba(0,0,0,.12))}
.ask-head{left:764px;top:402px;width:279px;height:80px;background:var(--blue-bright);text-align:center;color:var(--white);padding-top:14px}
.ask-head .ask-line1{font-family:'Oswald',sans-serif;font-size:19px;line-height:22px}
.ask-head .ask-line2{font-family:'Lato',sans-serif;font-size:19px;line-height:28px}
.field{left:787px;width:232px;height:27px;border:1px solid #d8d8d8;border-radius:3px;background:#fff;font-size:11px;color:#777;padding:6px 9px}
.field-msg{height:83px}
.ask-btn{left:868px;top:734px;width:72px;height:28px;background:var(--red);color:#fff;border-radius:3px;font-family:'Montserrat',sans-serif;font-weight:600;font-size:12px;text-align:center;line-height:28px;letter-spacing:1px}

/* reasons */
.why-title{left:0;top:852px;width:1200px;text-align:center;font-family:'Montserrat',sans-serif;font-weight:600;font-size:24px}
.reason{top:940px;width:260px;text-align:center}
.reason svg{display:block;margin:0 auto}
.reason h3{margin-top:20px;font-family:'Montserrat',sans-serif;font-weight:400;font-size:14.5px;letter-spacing:.8px}
.reason p{margin-top:10px;font-size:11.5px;line-height:16px;color:var(--grey-text)}

/* know your lawyer */
.lawyer-band{left:0;top:1191px;width:1200px;height:356px;background:var(--blue)}
.frame-back{left:156px;top:1258px;width:203px;height:203px;background:var(--blue-frame)}
.frame-front{left:181px;top:1283px;width:203px;height:203px;background:#2f6dbb}
.portrait{left:180px;top:1281px;width:179px;height:180px;background:linear-gradient(180deg,#f4f4f4 0%,#e6e6e6 50%,#2b2f3a 100%)}
.tagline{left:417px;top:1261px;font-family:'Montserrat',sans-serif;font-weight:700;font-size:19px;color:#fff;letter-spacing:.5px}
.tagline-sub{left:417px;top:1285px;font-family:'Montserrat',sans-serif;font-size:14px;color:#fff}
.about-text{left:417px;top:1316px;width:300px;font-size:11.5px;line-height:16px;color:#fff}
.about-more{left:417px;top:1455px;color:#fff}

/* practice areas */
.practice-card{left:765px;top:1161px;width:278px;height:418px;background:#f3f3f3;box-shadow:0 3px 10px rgba(0,0,0,.25)}
.practice-head{left:765px;top:1161px;width:278px;height:62px;background:linear-gradient(180deg,#3c433d,#252a26);color:#fff;font-family:'Montserrat',sans-serif;font-weight:600;font-size:24px;padding:17px 0 0 26px}
.practice-notch{left:807px;top:1222px}
.practice-item{left:796px;width:225px}
.practice-item h4{font-family:'Montserrat',sans-serif;font-weight:600;font-size:13.5px}
.practice-item p{margin-top:6px;font-size:11.5px;line-height:15.5px;color:var(--grey-text)}
.practice-more{left:796px;top:1530px;color:#444}

/* help */
.help-title{left:0;top:1652px;width:1200px;text-align:center;font-family:'Montserrat',sans-serif;font-weight:700;font-size:22px}
.help-sub{left:0;top:1684px;width:1200px;text-align:center;font-size:19px;color:#777}
.help-btn{left:495px;top:1735px;width:184px;height:37px;background:var(--orange);border-radius:3px;box-shadow:0 3px 6px rgba(0,0,0,.2);display:flex;align-items:center;justify-content:center;gap:10px;font-family:'Montserrat',sans-serif;font-weight:600;font-size:15px;color:#fff}

/* footer */
.site-footer{left:0;top:1858px;width:1200px;height:303px;background:var(--footer)}
.foot-title{top:1920px;font-family:'Montserrat',sans-serif;font-size:14px;color:#eee;letter-spacing:1px}
.foot-links{left:156px;top:1956px;list-style:none;font-size:12px;color:var(--footer-text)}
.foot-links li{height:22px;padding-left:16px;position:relative}
.foot-links li::before{content:"";position:absolute;left:2px;top:6px;width:5px;height:5px;border-radius:50%;background:var(--footer-text)}
.foot-links li.is-hover{color:var(--red)}
.foot-links li.is-hover::before{background:var(--red)}
.foot-field{left:460px;width:203px;height:26px;border:1px solid #8a8a8a;border-radius:3px;font-size:11px;color:#bbb;padding:6px 9px}
.foot-submit{left:460px;top:2050px;width:87px;height:26px;background:#2a2a2a;color:#fff;border-radius:3px;font-family:'Montserrat',sans-serif;font-weight:600;font-size:11px;text-align:center;line-height:26px;letter-spacing:1px}
.foot-contact{left:764px;top:1956px;font-size:12px;line-height:16px;color:var(--footer-text)}
.foot-social-label{left:764px;top:2069px;font-size:12.5px;color:#ddd}
.foot-social{left:764px;top:2099px;display:flex;gap:6px}
.foot-social span{width:24px;height:24px;border-radius:50%;background:#d4d4d4}
.footer-bottom{left:0;top:2161px;width:1200px;height:64px;background:var(--footer-bottom)}
.copyright{left:156px;top:2186px;font-size:11.5px;color:#a8a8a8}
.copyright .legal{color:#d0d0d0}
.to-top{left:1005px;top:2180px;width:26px;height:26px;border:2px solid #bbb;border-radius:50%}
</style>
</head>
<body>

<header class="site-header abs">
  <div class="brand abs">The Thornwell Law Group</div>
  <div class="social-top abs" aria-label="Social links">
    <span class="social-dot"></span><span class="social-dot is-active"></span><span class="social-dot"></span><span class="social-dot"></span>
  </div>
  <div class="call abs">
    <span class="call-label">Call</span>
    <svg width="28" height="28" viewBox="0 0 28 28"><circle cx="14" cy="14" r="12" fill="none" stroke="var(--red)" stroke-width="2.4"/><path d="M9.5 8.5c1-1 2-1 2.6 0l1 1.8c.4.7.2 1.3-.4 1.8l-.7.5c.6 1.5 1.8 2.8 3.4 3.5l.5-.7c.5-.6 1.1-.8 1.8-.4l1.8 1c1 .6 1 1.6 0 2.6-1.5 1.5-4 1-6.6-1.6s-3.1-5.1-1.6-6.5z" fill="var(--red)"/></svg>
    <span>504-917-2083</span>
  </div>
</header>

<nav class="main-nav abs">
  <ul>
    <li class="is-current">HOME</li>
    <li>ABOUT MY FIRM</li>
    <li>ATTORNEY BIO</li>
    <li>PERSONAL INJURY</li>
    <li>TESTIMONIALS</li>
    <li>BLOG</li>
    <li>CONTACT US</li>
  </ul>
</nav>

<section class="hero abs" role="img" aria-label="Photo of a lawyer's hands signing a document with a fountain pen beside a wooden stamp on a desk"></section>
<h1 class="hero-title abs">Goals and Belief</h1>
<p class="hero-text abs">We Belive in "KNOW YOUR LAWYER" and with this serving clients who needs to handle car accident and general personal injury lawsuits.</p>
<div class="hero-more read-more abs"><svg width="10" height="10" viewBox="0 0 10 10"><circle cx="5" cy="5" r="5" fill="#fff"/><path d="M4 3l2 2-2 2" stroke="#333" stroke-width="1.3" fill="none"/></svg>READ MORE</div>
<svg class="arrow-left abs" width="22" height="22" viewBox="0 0 22 22"><path d="M20 11H3M10 4l-7 7 7 7" stroke="#fff" stroke-width="2.6" fill="none"/></svg>
<svg class="arrow-right abs" width="22" height="22" viewBox="0 0 22 22"><path d="M2 11h17M12 4l7 7-7 7" stroke="var(--red)" stroke-width="2.6" fill="none"/></svg>

<section class="testimonials abs"></section>
<h2 class="section-label abs">Client Testimonials</h2>
<p class="quote abs">"&nbsp;Hiring Daniel Marsh was one of the best decisions of my life. From the first moment I spoke to Daniel, I knew he was the attorney for me. I felt he was honest and caring. He also took extra care..."</p>
<div class="avatar abs" role="img" aria-label="Client portrait"></div>
<div class="client-name abs">— Karen L.</div>
<div class="slider-dots abs"><span></span><span></span><span class="is-on"></span><span></span><span></span></div>

<svg class="ask-card abs" width="279" height="411" viewBox="0 0 279 411"><path d="M0 0H279V347L139.5 411 0 347Z" fill="#fff"/></svg>
<div class="ask-head abs"><div class="ask-line1">“Quick Question? Quick Answer”</div><div class="ask-line2">Contact Us Today!</div></div>
<div class="field abs" style="top:505px">Name</div>
<div class="field abs" style="top:542px">Email</div>
<div class="field abs" style="top:579px">Phone</div>
<div class="field field-msg abs" style="top:617px">Your Question ...</div>
<div class="ask-btn abs">ASK</div>

<h2 class="why-title abs">Why - The Thornwell Law Group?</h2>
<div class="reason abs" style="left:167px">
  <svg width="52" height="62" viewBox="0 0 52 62" fill="none" stroke="var(--red)" stroke-width="3"><rect x="14" y="4" width="22" height="14" rx="2" transform="rotate(-20 25 11)"/><path d="M8 32l14-10 10 4c3 1 3 5 0 5h-9M8 32l-4 12 10 12 18-6 14-16c2-3-1-6-4-4l-10 8"/></svg>
  <h3>LESS CHARGE</h3>
  <p>We charge less to our clients so they<br>keep more for future</p>
</div>
<div class="reason abs" style="left:470px">
  <svg width="52" height="64" viewBox="0 0 52 64" fill="none" stroke="var(--red)" stroke-width="3"><circle cx="26" cy="24" r="19"/><circle cx="26" cy="24" r="11"/><path d="M14 40l-6 20 8-4 5 7 5-19M38 40l6 20-8-4-5 7-5-19"/></svg>
  <h3>EXPERIENCE &amp; SUCCESS</h3>
  <p>We have experience and success trying and<br>settling multi-million dollar cases</p>
</div>
<div class="reason abs" style="left:773px">
  <svg width="60" height="60" viewBox="0 0 60 60" fill="none" stroke="var(--red)" stroke-width="3"><path d="M25 4h10l2 8 6 3 7-4 7 7-4 7 3 6 8 2v10l-8 2-3 6 4 7-7 7-7-4-6 3-2 8H25l-2-8-6-3-7 4-7-7 4-7-3-6-8-2V25l8-2 3-6-4-7 7-7 7 4 6-3z" transform="translate(1 1) scale(.96)"/><circle cx="30" cy="30" r="10"/></svg>
  <h3>USE MODERN TECHNOLOGY</h3>
  <p>We use modern technology to make the whole<br>process simple, easy and hassle-free</p>
</div>

<section class="lawyer-band abs"></section>
<div class="frame-back abs"></div>
<div class="frame-front abs"></div>
<div class="portrait abs" role="img" aria-label="Portrait of the attorney in a dark suit and tie"></div>
<h2 class="tagline abs">“KNOW YOUR LAWYER”</h2>
<div class="tagline-sub abs">About Us</div>
<p class="about-text abs">Lorem Ipsum is simply dummy text of the printing and typesetting industry. Lorem Ipsum has been the industry's standard dummy text ever since the 1500s, when an unknown printer took a galley of type and scrambled it to make a type specimen book. It has survived not only five centuries, but also the leap into electronic typesetting, ...</p>
<div class="about-more read-more abs"><svg width="10" height="10" viewBox="0 0 10 10"><circle cx="5" cy="5" r="5" fill="#fff"/><path d="M4 3l2 2-2 2" stroke="var(--blue)" stroke-width="1.3" fill="none"/></svg>READ MORE</div>

<div class="practice-card abs"></div>
<div class="practice-head abs">Practice Areas</div>
<svg class="practice-notch abs" width="24" height="13" viewBox="0 0 24 13"><path d="M0 0h24L12 13z" fill="#252a26"/></svg>
<div class="practice-item abs" style="top:1263px"><h4>1. Car Accidents</h4><p>Lorem Ipsum is simply dummy text of the printing and typesetting industry. Lorem Ipsum has been the industry's standard dummy text ever since the 1500s.</p></div>
<div class="practice-item abs" style="top:1391px"><h4>2. General Personal Injury</h4><p>Lorem Ipsum is simply dummy text of the printing and typesetting industry. Lorem Ipsum has been the industry's standard dummy text ever since the 1500s.</p></div>
<div class="practice-more read-more abs"><svg width="10" height="10" viewBox="0 0 10 10"><circle cx="5" cy="5" r="5" fill="#333"/><path d="M4 3l2 2-2 2" stroke="#fff" stroke-width="1.3" fill="none"/></svg>READ MORE</div>

<h2 class="help-title abs">Can We Help You?</h2>
<p class="help-sub abs">We are available to answer your question 24/7 ...</p>
<div class="help-btn abs">
  <svg width="18" height="18" viewBox="0 0 18 18"><path d="M4 2c1-1 2-1 2.6 0l1.2 2c.4.7.2 1.3-.4 1.8l-.8.6c.7 1.8 2.1 3.2 3.8 3.9l.6-.8c.5-.6 1.1-.8 1.8-.4l2 1.2c1 .6 1 1.6 0 2.6-1.7 1.7-4.6 1.2-7.5-1.7S2.3 3.7 4 2z" fill="#fff"/></svg>
  504-917-2083
</div>

<footer class="site-footer abs"></footer>
<h3 class="foot-title abs" style="left:156px">SITE INFORMATION</h3>
<h3 class="foot-title abs" style="left:460px">NEWSLETTER</h3>
<h3 class="foot-title abs" style="left:764px">CONTACT INFO</h3>
<ul class="foot-links abs">
  <li>Home</li><li class="is-hover">About My Firm</li><li>Attorney Bio</li><li>Personal Injury</li><li>Testimonials</li><li>Blog</li><li>Contact</li>
</ul>
<div class="foot-field abs" style="top:1962px">Name</div>
<div class="foot-field abs" style="top:2000px">Email</div>
<div class="foot-submit abs">SUBMIT</div>
<div class="foot-contact abs">Thornwell Law Group<br>2140 Larkspur Ave. NE Suite B<br>Albuquerque, NM 87110<br><br>Phone: 504-917-2083<br>Email: info@thornwelllawgroup.com</div>
<div class="foot-social-label abs">Get Social:</div>
<div class="foot-social abs"><span></span><span></span><span></span><span></span></div>
<div class="footer-bottom abs"></div>
<p class="copyright abs">© 2016 by Thornwell Law Group. All rights reserved. &nbsp;<span class="legal">Disclaimer &nbsp;/&nbsp; Site Map &nbsp;/&nbsp; Privacy Policy</span></p>
<svg class="to-top abs" width="26" height="26" viewBox="0 0 26 26"><path d="M11 17V9M7 12l4-4 4 4" stroke="#bbb" stroke-width="2" fill="none"/></svg>

</body>
</html>
```